Flu 2019

Lockridge Regional Hospital is hosting a health fair/flu shot clinic this Fall. What she'd like to convey is the following:

Health Fair & Flu Clinic 2019
At the following locations from 10am - 1pm
Cedar Bluff - September 25 at Courthouse in Cedar Bluff
Harlow - October 2 at Harlow Multipurpose Center
Tasker - October 9 at Tasker Community Center
No cost flu shots available. Please bring insurance information.
Door prizes - Giveaways - Treats
Brought to you by Lockridge Regional Hospital

We would like to highlight the health fair which will be free to the community. We would like to also highlight the flu clinic; however, the no cost/bring insurance needs to be in smaller print.

```html
<!DOCTYPE html>
<html lang="en">
<head>
<meta charset="utf-8">
<title>Health Fair &amp; Flu Clinic 2019 – Lockridge Regional Hospital</title>
<link rel="stylesheet" href="https://fonts.googleapis.com/css2?family=Ultra&family=Oswald:wght@500;600&family=Open+Sans:wght@600;700&display=swap">
<style>
  :root {
    --red: #b3272a;
    --red-soft: #c23a34;
    --accent: #ec5a3c;
    --navy: #151a36;
    --navy-mid: #33385a;
    --ink: #1d1d1f;
    --white: #ffffff;
    --photo-light: #d5dddd;
    --photo-mid: #8fa7c2;
    --photo-deep: #4f6f9a;
  }
  * { margin: 0; padding: 0; box-sizing: border-box; }
  html, body { width: 1009px; height: 1200px; overflow: hidden; background: var(--white); }
  .flyer { position: relative; width: 1009px; height: 1200px; background: var(--white); font-family: "Open Sans", sans-serif; color: var(--ink); }

  .header { position: absolute; left: 0; top: 0; width: 1009px; height: 200px; z-index: 3; }
  .brand { position: absolute; left: 62px; top: 46px; display: flex; align-items: center; gap: 14px; z-index: 4; }
  .brand-dot { width: 40px; height: 40px; border-radius: 50%; background: var(--ink); }
  .brand-name { font-family: "Oswald", sans-serif; font-weight: 600; font-size: 30px; line-height: 1.05; color: var(--ink); width: 220px; }
  .header-title { position: absolute; right: 30px; top: 48px; font-family: "Oswald", sans-serif; font-weight: 600; font-size: 30px; color: var(--red); z-index: 4; letter-spacing: .3px; }

  .hero { position: absolute; left: 0; top: 110px; width: 1009px; height: 657px; background: linear-gradient(90deg, var(--navy) 0%, var(--navy-mid) 36%, #7f8595 46%, var(--photo-light) 54%); overflow: hidden; }
  .hero-photo { position: absolute; right: 0; top: 0; width: 560px; height: 657px; background: linear-gradient(180deg, var(--photo-light) 0%, var(--photo-mid) 45%, var(--photo-deep) 100%); -webkit-mask-image: linear-gradient(90deg, transparent 0, #000 90px); mask-image: linear-gradient(90deg, transparent 0, #000 90px); }
  .hero-copy { position: absolute; left: 48px; top: 210px; color: var(--white); }
  .hero-kicker { font-family: "Oswald", sans-serif; font-weight: 500; font-size: 29px; letter-spacing: .5px; }
  .hero-headline { font-family: "Ultra", serif; font-weight: 400; font-size: 84px; line-height: 106px; letter-spacing: 5px; margin-top: 14px; text-shadow: 0 3px 6px rgba(0,0,0,.35); }
  .hero-headline .accent { color: var(--accent); }

  .locations { position: absolute; left: 0; top: 767px; width: 1009px; height: 213px; display: grid; grid-template-columns: repeat(3, 1fr); }
  .location { background: var(--red); color: var(--white); text-align: center; padding-top: 20px; }
  .location:nth-child(2) { background: var(--red-soft); }
  .location-icon { width: 44px; height: 42px; display: block; margin: 0 auto 14px; }
  .location-town { font-weight: 700; font-size: 36px; line-height: 1.1; margin-bottom: 8px; }
  .location-detail { font-weight: 700; font-size: 17px; line-height: 1.55; text-transform: uppercase; }
  .location-time { font-weight: 700; font-size: 17px; line-height: 1.55; }

  .perks { position: absolute; left: 50px; top: 1022px; list-style: none; }
  .perk { display: flex; align-items: center; gap: 14px; font-weight: 600; font-size: 23px; margin-bottom: 22px; }
  .perk svg { width: 22px; height: 22px; flex: none; }
  .perk small { font-size: 15px; font-weight: 600; }

  .vaccine-photo { position: absolute; left: 748px; top: 995px; width: 190px; height: 190px; border-radius: 50%; border: 5px solid var(--red); background: linear-gradient(135deg, #e9eef2 0%, #c9a590 50%, #6d97cf 100%); }
  .footer-bar { position: absolute; left: 0; bottom: 0; width: 1009px; height: 10px; background: var(--ink); }
</style>
</head>
<body>
<main class="flyer">
  <section class="hero">
    <div class="hero-photo" role="img" aria-label="Photo of a sick man wrapped in a striped blue blanket, with a syringe graphic beside the headline"></div>
    <div class="hero-copy">
      <p class="hero-kicker">HEALTH FAIR &amp; FLU CLINIC 2019</p>
      <h1 class="hero-headline">FREE<br><span class="accent">FLUE</span><br>SHOT</h1>
    </div>
  </section>

  <svg class="header" viewBox="0 0 1009 200" preserveAspectRatio="none" aria-hidden="true">
    <path d="M0 0 H1009 V120 C820 165 600 215 340 180 C210 162 90 160 0 176 Z" fill="#ffffff"/>
    <path d="M0 176 C90 160 210 162 340 180 C600 215 820 165 1009 120 V142 C820 192 600 236 340 200 C210 183 90 182 0 196 Z" fill="#b3272a"/>
  </svg>

  <div class="brand">
    <span class="brand-dot"></span>
    <span class="brand-name">Lockridge Regional Hospital</span>
  </div>
  <p class="header-title">HEALTH FAIR &amp; FLU CLINIC 2019</p>

  <section class="locations">
    <article class="location">
      <svg class="location-icon" viewBox="0 0 44 42" aria-hidden="true"><rect x="2" y="5" width="40" height="35" rx="3" fill="#fff"/><rect x="2" y="5" width="40" height="9" fill="#f3d4d0"/><g fill="#b3272a"><rect x="9" y="19" width="5" height="4"/><rect x="17" y="19" width="5" height="4"/><rect x="25" y="19" width="5" height="4"/><rect x="33" y="19" width="4" height="4"/><rect x="9" y="27" width="5" height="4"/><rect x="17" y="27" width="5" height="4"/><rect x="25" y="27" width="5" height="4"/></g><rect x="11" y="1" width="4" height="9" rx="2" fill="#fff"/><rect x="29" y="1" width="4" height="9" rx="2" fill="#fff"/></svg>
      <h2 class="location-town">CEDAR BLUFF</h2>
      <p class="location-detail">September 25<br>at Courthouse</p>
      <p class="location-time">from 10am - 1pm</p>
    </article>
    <article class="location">
      <svg class="location-icon" viewBox="0 0 44 42" aria-hidden="true"><rect x="2" y="5" width="40" height="35" rx="3" fill="#fff"/><rect x="2" y="5" width="40" height="9" fill="#f3d4d0"/><g fill="#b3272a"><rect x="9" y="19" width="5" height="4"/><rect x="17" y="19" width="5" height="4"/><rect x="25" y="19" width="5" height="4"/><rect x="33" y="19" width="4" height="4"/><rect x="9" y="27" width="5" height="4"/><rect x="17" y="27" width="5" height="4"/><rect x="25" y="27" width="5" height="4"/></g><rect x="11" y="1" width="4" height="9" rx="2" fill="#fff"/><rect x="29" y="1" width="4" height="9" rx="2" fill="#fff"/></svg>
      <h2 class="location-town">HARLOW</h2>
      <p class="location-detail">October 2<br>at Harlow Multipurpose Center</p>
      <p class="location-time">from 10am - 1pm</p>
    </article>
    <article class="location">
      <svg class="location-icon" viewBox="0 0 44 42" aria-hidden="true"><rect x="2" y="5" width="40" height="35" rx="3" fill="#fff"/><rect x="2" y="5" width="40" height="9" fill="#f3d4d0"/><g fill="#b3272a"><rect x="9" y="19" width="5" height="4"/><rect x="17" y="19" width="5" height="4"/><rect x="25" y="19" width="5" height="4"/><rect x="33" y="19" width="4" height="4"/><rect x="9" y="27" width="5" height="4"/><rect x="17" y="27" width="5" height="4"/><rect x="25" y="27" width="5" height="4"/></g><rect x="11" y="1" width="4" height="9" rx="2" fill="#fff"/><rect x="29" y="1" width="4" height="9" rx="2" fill="#fff"/></svg>
      <h2 class="location-town">TASKER</h2>
      <p class="location-detail">October 9<br>at Tasker Community Center</p>
      <p class="location-time">from 10am - 1pm</p>
    </article>
  </section>

  <ul class="perks">
    <li class="perk"><svg viewBox="0 0 22 22" aria-hidden="true"><circle cx="11" cy="11" r="9" fill="none" stroke="#b3272a" stroke-width="2"/><path d="M6.5 11 L10 14.5 L15.5 8" fill="none" stroke="#b3272a" stroke-width="2.2"/></svg><span>No cost flu shots available. <small>Please bring insurance information</small></span></li>
    <li class="perk"><svg viewBox="0 0 22 22" aria-hidden="true"><circle cx="11" cy="11" r="9" fill="none" stroke="#b3272a" stroke-width="2"/><path d="M6.5 11 L10 14.5 L15.5 8" fill="none" stroke="#b3272a" stroke-width="2.2"/></svg><span>Door prizes - Giveaways - Treats</span></li>
    <li class="perk"><svg viewBox="0 0 22 22" aria-hidden="true"><circle cx="11" cy="11" r="9" fill="none" stroke="#b3272a" stroke-width="2"/><path d="M6.5 11 L10 14.5 L15.5 8" fill="none" stroke="#b3272a" stroke-width="2.2"/></svg><span>Brought to you by Lockridge Regional Hospital</span></li>
  </ul>

  <div class="vaccine-photo" role="img" aria-label="Photo of a gloved hand giving a vaccine injection in an upper arm"></div>
  <div class="footer-bar"></div>
</main>
</body>
</html>
```